Roaming Kestrel (hail repair) Company seeks Web design

We are looking for someone to design a website for an automotive hail damage repair business. We are a national company that travels to cities that have suffered a catastrophic hail event, where we set up for retail customers to come in and have all of their auto hail repair needs handled.
We had a website in the past, but due to a technical error it has been deleted. You can view the old webpage by going to old.pagevault.net and searching www.Pellet-Yard.com and looking under the date June 3rd 2015. We are hoping to have something similar to the original, but more extensive and updated. We would also like to add a page that allows our customers to get an online estimate by filling in their own damage assessment. There is a great example of what we are looking for if you go to www.smoothcoatworkshop.com and click on "Get An Estimate".

Target Market(s)

USA

Industry/Entity Type

Automotive

Number of Pages Required

5+ page

Requirements
Must have
• Mobile Friendly, easy for me to change locations on the location page along with the map. A link to google maps app from site.

```html
<!DOCTYPE html>
<html lang="en">
<head>
<meta charset="utf-8">
<title>Pellet Yard – Hail Repair</title>
<link rel="stylesheet" href="https://fonts.googleapis.com/css2?family=Bebas+Neue&family=Open+Sans:ital,wght@0,400;0,600;0,700;0,800;1,400;1,700&display=swap">
<style>
:root{
  --yellow:#d8b81c;
  --navy:#2d4a5f;
  --nav:#4b6d88;
  --red:#d42b1f;
  --ink:#222;
  --dark:#1c2833;
  --footer:#1f2b37;
  --grey:#6f7274;
  --light:#f3f3f3;
  --blue-text:#6fb4e0;
}
*{box-sizing:border-box;margin:0;padding:0}
html,body{width:1200px;height:3571px;overflow:hidden}
body{font-family:'Open Sans',sans-serif;color:var(--ink);background:#fff;position:relative}
.abs{position:absolute}
.display{font-family:'Bebas Neue',sans-serif;letter-spacing:1px;font-weight:400}

/* header */
.site-header{top:0;left:0;width:1200px;height:131px;background:#fff}
.brand{left:100px;top:34px;display:flex;align-items:center;gap:10px}
.brand-mark{width:22px;height:22px;background:var(--yellow)}
.brand-name{font-family:'Bebas Neue',sans-serif;font-size:46px;color:var(--ink);line-height:1}
.brand-tag{left:132px;top:84px;font-size:10px;color:#777}
.why{left:358px;top:26px;font-size:17px;line-height:1.1;color:#2b4b66;font-weight:600}
.why b{display:block;font-size:28px;font-weight:800}
.perks{left:358px;top:78px;font-size:12px;color:#333}
.cart{left:650px;top:40px;font-size:20px;color:var(--red);font-weight:800}
.social-top{left:1034px;top:30px;display:flex;gap:5px}
.social-top span{width:15px;height:15px;background:#4b6d88;display:block}
.contact-top{left:930px;top:60px;font-size:13px;color:#333;text-align:right;width:170px;line-height:1.6}
.contact-top em{color:#3a7cb0;font-style:italic}

/* nav */
.main-nav{top:131px;left:0;width:1200px;height:59px;background:var(--nav);border-top:3px solid var(--yellow)}
.main-nav ul{list-style:none;display:flex;position:absolute;left:240px;top:0;height:56px}
.main-nav li{color:#fff;font-size:15px;font-weight:700;padding:0 26px;line-height:56px}
.main-nav li.active{background:var(--yellow);padding:0 30px}

/* hero */
.hero{top:190px;left:0;width:1200px;height:453px;background:linear-gradient(100deg,#3a1414 0%,#6e1c1c 22%,#2e2a2a 45%,#3b3e44 70%,#22262b 100%)}
.hero-shade{top:190px;left:0;width:1200px;height:453px;background:rgba(0,0,0,.35)}
.hero-title{top:240px;left:0;width:1200px;text-align:center;color:#fff;font-size:44px}
.field{color:#fff;font-size:15px;font-weight:600}
.field .select{margin-top:8px;width:393px;height:38px;background:#fff;border:1px solid #ccc;font-size:14px;font-weight:400;color:#999;padding:9px 14px;position:relative}
.field .select::after{content:"";position:absolute;right:14px;top:16px;border:5px solid transparent;border-top:6px solid #666}
.continue{left:614px;top:519px;width:400px;height:40px;background:var(--yellow);color:#fff;font-weight:800;font-size:15px;text-align:center;line-height:40px}

/* features */
.pattern{top:643px;left:0;width:1200px;height:845px;background:#fbfbfb}
.feature{width:314px;height:207px;background:var(--navy);color:#fff;text-align:center;padding:68px 20px 0;top:757px;border-bottom:4px solid #1a2d3b}
.feature.alt{background:var(--yellow);border-bottom-color:#a98e0e}
.feature h3{font-size:13px;font-weight:800;text-transform:uppercase}
.feature h4{font-size:12px;font-style:italic;color:var(--blue-text);font-weight:700;margin-bottom:8px}
.feature.alt h4{color:#fff}
.feature p{font-size:12px;font-weight:700;line-height:1.4}
.feature .search{position:absolute;bottom:16px;left:0;width:100%;font-size:14px;font-weight:800;color:var(--blue-text)}
.feature.alt .search{color:#fff}
.feature-icon{width:86px;height:86px;border-radius:50%;background:#fff;top:695px;display:flex;align-items:center;justify-content:center}

.about-title{top:1045px;width:1200px;text-align:center;font-size:58px;color:var(--navy)}
.about-sub{top:1106px;width:1200px;text-align:center;font-size:20px;color:var(--red);font-style:italic}
.body-copy{left:110px;width:980px;font-size:13.5px;text-align:center;line-height:1.6}
.carousel{top:1226px;left:0;width:1200px;height:95px;background:#e9e9e9}
.part{top:1240px;width:90px;height:66px;background:linear-gradient(#c8c8c8,#8e8e8e);border-radius:6px}

/* categories */
.cats{top:1488px;left:0;width:1200px;height:638px;background:linear-gradient(180deg,#1f2c38,#2d3a46 50%,#1a242d)}
.cats-title{top:1548px;width:1200px;text-align:center;color:#fff;font-size:50px}
.cats-sub{top:1613px;width:1200px;text-align:center;color:var(--blue-text);font-size:19px;font-style:italic;font-weight:700}
.cat{top:1755px;width:314px;height:97px;background:var(--navy);color:#fff;font-family:'Bebas Neue',sans-serif;font-size:30px;text-align:center;padding-top:46px;border:1px solid #4d6a80}
.cat-img{top:1667px;width:128px;height:128px;border-radius:50%;background:radial-gradient(#aaa,#333);border:4px solid #fff}
.view-all{left:440px;top:1933px;width:317px;height:103px;background:var(--yellow);color:#fff;font-family:'Bebas Neue',sans-serif;font-size:30px;text-align:center;line-height:103px}

/* testimonial */
.say-label{left:98px;top:2188px;font-size:20px}
.video-label{left:795px;top:2188px;font-size:20px}
.quote{left:95px;top:2250px;width:536px;height:214px;background:#e6e6e6;padding:30px 40px 0 110px}
.quote p{font-size:15px;font-style:italic;font-weight:700;line-height:1.7}
.quote .who{margin-top:14px;font-size:14px}
.quote .who b{color:var(--blue-text);font-size:24px}
.laptop-screen{left:672px;top:2226px;width:370px;height:238px;background:#111;border-radius:10px;padding:14px}
.laptop-screen div{width:100%;height:100%;background:linear-gradient(#3d4652,#5c6670)}
.laptop-base{left:614px;top:2464px;width:486px;height:20px;background:linear-gradient(#ddd,#999);border-radius:0 0 40px 40px}

/* signup */
.signup{top:2579px;left:0;width:1200px;height:373px;background:linear-gradient(180deg,#3a4652,#262f38)}
.signup-title{top:2646px;width:1200px;text-align:center;color:#fff;font-size:56px}
.signup-sub{top:2710px;width:1200px;text-align:center;color:#fff;font-size:19px;font-style:italic;font-weight:700}
.email{left:269px;top:2779px;width:398px;height:50px;background:#1b232b;color:#888;font-size:14px;padding:15px 20px}
.subscribe{left:679px;top:2779px;width:250px;height:50px;background:var(--yellow);color:#fff;font-family:'Bebas Neue',sans-serif;font-size:24px;line-height:50px;text-align:center}

/* footer */
.site-footer{top:2952px;left:0;width:1200px;height:405px;background:var(--footer)}
.fcol{top:2990px;width:250px;color:#9fb0bd;font-size:12.5px}
.fcol h5{color:#fff;font-family:'Bebas Neue',sans-serif;font-size:18px;font-weight:400;margin-bottom:12px}
.fcol li{list-style:none;line-height:25.7px}
.fcol li::before{content:"» ";color:#fff}
.fcol p{line-height:1.5;margin-bottom:10px}
.fcol p b{color:#fff}
.pay-bar{top:3357px;left:0;width:1200px;height:95px;background:var(--grey)}
.accept{left:98px;top:3392px;color:#fff;font-family:'Bebas Neue',sans-serif;font-size:24px;display:flex;align-items:center;gap:6px}
.accept span{width:38px;height:22px;background:#eee;border-radius:3px;display:block}
.social-bottom{left:990px;top:3393px;display:flex;gap:6px}
.social-bottom span{width:22px;height:22px;background:#2d4a8f;display:block}
.legal{top:3452px;left:0;width:1200px;height:119px;background:var(--yellow);text-align:center;font-size:12px;color:#222;padding-top:40px;line-height:2.2}
</style>
</head>
<body>

<header class="abs site-header">
  <div class="abs brand"><span class="brand-mark"></span><span class="brand-name">PELLET YARD</span></div>
  <div class="abs brand-tag">Hail repair done right</div>
  <div class="abs why">Why Shop<b>WITH US?</b></div>
  <div class="abs perks">✓ Affordable Prices &nbsp;/&nbsp; ☐ Huge Selection &nbsp;/&nbsp; ⟳ Expert Support</div>
  <div class="abs cart">🛒 CART ▾</div>
  <div class="abs social-top"><span></span><span></span><span></span><span></span></div>
  <div class="abs contact-top"><em>Call Us:</em> <b>1-000-000-0000</b><br><em>Email Us:</em> info@pelletyard.com</div>
</header>

<nav class="abs main-nav">
  <ul><li class="active">HOME</li><li>ABOUT US</li><li>OUR MISSION</li><li>HAIL REPAIR SERVICES</li><li>CONTACT</li></ul>
</nav>

<section>
  <div class="abs hero" role="img" aria-label="Photo of a red car being repaired in a workshop"></div>
  <div class="abs hero-shade"></div>
  <h1 class="abs display hero-title">GENERATE AN ESTIMATE</h1>
  <div class="abs field" style="left:190px;top:347px">Hood:<div class="select">Select Year...</div></div>
  <div class="abs field" style="left:614px;top:347px">Roof:<div class="select">Select Make...</div></div>
  <div class="abs field" style="left:190px;top:433px">Metal Sunroof:<div class="select">Select Model...</div></div>
  <div class="abs field" style="left:614px;top:433px">Deck Lid:<div class="select">Select Part...</div></div>
  <div class="abs continue">CONTINUE ⚲</div>
</section>

<section>
  <div class="abs pattern"></div>
  <div class="abs feature-icon" style="left:212px"><svg width="70" height="70" viewBox="0 0 70 70"><circle cx="35" cy="35" r="30" fill="var(--navy)"/><circle cx="35" cy="35" r="22" fill="none" stroke="#fff" stroke-width="2"/></svg></div>
  <div class="abs feature-icon" style="left:555px"><svg width="60" height="60" viewBox="0 0 60 60"><path d="M16 38a9 9 0 0 1 2-18 13 13 0 0 1 25 3 8 8 0 0 1 1 15z" fill="none" stroke="#222" stroke-width="3"/><path d="M31 30l-6 10h7l-4 10" fill="none" stroke="#222" stroke-width="3"/></svg></div>
  <div class="abs feature-icon" style="left:898px"><svg width="60" height="60" viewBox="0 0 60 60"><circle cx="26" cy="24" r="14" fill="none" stroke="#3a7cb0" stroke-width="4"/><path d="M36 34l14 14" stroke="#3a7cb0" stroke-width="6"/></svg></div>

  <div class="abs feature" style="left:98px"><h3>Satisfaction Guaranteed</h3><h4>Are you looking for a local salvage yard?</h4><p>Lorem Ipsum is simply dummy text of the printing and typesetting industry. Lorem Ipsum has been the industry's standard...</p><div class="search">SEARCH</div></div>
  <div class="abs feature alt" style="left:440px"><h3>Another Hail Storm</h3><h4>Lorem Ipsum is simply dummy text</h4><p>Lorem Ipsum is simply dummy text of the printing and typesetting industry. Lorem Ipsum has been the industry's standard...</p><div class="search">SEARCH</div></div>
  <div class="abs feature" style="left:783px"><h3>Attentation to Detail</h3><h4>Lorem Ipsum is simply dummy text</h4><p>Lorem Ipsum is simply dummy text of the printing and typesetting industry. Lorem Ipsum has been the industry's standard...</p><div class="search">SEARCH</div></div>

  <h2 class="abs display about-title">ABOUT PELLET YARD</h2>
  <div class="abs about-sub">Lorem Ipsum is simply dummy text of the printing and typesetting industry</div>
  <p class="abs body-copy" style="top:1160px">Lorem Ipsum is simply dummy text of the printing and typesetting industry. Lorem Ipsum has been the industry's standard dummy text ever since the 1500s, when an unknown printer took a galley of type and scrambled it to make a type specimen book.</p>
  <div class="abs carousel"></div>
  <svg class="abs" style="left:148px;top:1262px" width="14" height="20"><path d="M11 2L3 10l8 8" fill="none" stroke="#999" stroke-width="2"/></svg>
  <svg class="abs" style="left:1040px;top:1262px" width="14" height="20"><path d="M3 2l8 8-8 8" fill="none" stroke="var(--red)" stroke-width="2"/></svg>
  <div class="abs part" role="img" aria-label="Auto part: oil filter" style="left:210px"></div>
  <div class="abs part" role="img" aria-label="Auto part: spark plug wires" style="left:320px"></div>
  <div class="abs part" role="img" aria-label="Auto part: coil spring" style="left:430px"></div>
  <div class="abs part" role="img" aria-label="Auto part: bushings" style="left:580px"></div>
  <div class="abs part" role="img" aria-label="Auto part: CV boots" style="left:690px"></div>
  <div class="abs part" role="img" aria-label="Auto part: CV joint" style="left:820px"></div>
  <div class="abs part" role="img" aria-label="Auto part: ball joint" style="left:930px"></div>
  <p class="abs body-copy" style="top:1340px">Lorem Ipsum is simply dummy text of the printing and typesetting industry. Lorem Ipsum has been the industry's standard dummy text ever since the 1500s, when an unknown printer took a galley of type and scrambled it to make a type specimen book. It has survived not only five centuries, but also the leap into electronic typesetting, remaining essentially unchanged. It was popularised in the 1960s with the release</p>
</section>

<section>
  <div class="abs cats" role="img" aria-label="Dark photo of a salvage yard full of cars"></div>
  <h2 class="abs display cats-title">WHEN PERFECTION MEETS A STANDARD</h2>
  <div class="abs cats-sub">Lorem Ipsum is simply dummy text of the printing and typesetting industry.</div>
  <div class="abs cat" style="left:98px">DO IT YOURSELF...</div>
  <div class="abs cat" style="left:440px">WHAT IS PDR?</div>
  <div class="abs cat" style="left:783px">ANOTHER STORM</div>
  <div class="abs cat-img" role="img" aria-label="Photo of a car engine part" style="left:191px"></div>
  <div class="abs cat-img" role="img" aria-label="Photo of a red car hood" style="left:534px;background:radial-gradient(#e04a3a,#5a1010)"></div>
  <div class="abs cat-img" role="img" aria-label="Photo of assorted engine components" style="left:876px"></div>
  <svg class="abs" style="left:567px;top:1890px" width="64" height="64" viewBox="0 0 64 64"><circle cx="32" cy="32" r="30" fill="var(--red)"/><path d="M18 32h24M32 20l12 12-12 12" fill="none" stroke="#111" stroke-width="6"/></svg>
  <div class="abs view-all">VIEW ALL CATEGORIES</div>
</section>

<section>
  <div class="abs say-label">What People <b>Saying?</b></div>
  <div class="abs video-label">Watch <b>Video</b></div>
  <div class="abs quote">
    <svg class="abs" style="left:32px;top:32px" width="50" height="40"><path d="M4 36V20C4 10 10 4 20 4v8c-5 0-8 3-8 8h8v16zM28 36V20c0-10 6-16 16-16v8c-5 0-8 3-8 8h8v16z" fill="#bbb"/></svg>
    <p>"Lorem Ipsum is simply dummy text of the printing and typesetting industry. Lorem Ipsum has been the industry's standard dummy text ever since the 1500s, when an unknown printer took a galley."</p>
    <div class="who"><b><i>Dale Porter,</i></b> <i>Lorem Ipsum</i></div>
  </div>
  <svg class="abs" style="left:95px;top:2474px" width="60" height="18"><path d="M2 9h22M8 3L2 9l6 6" fill="none" stroke="#999" stroke-width="2"/><path d="M32 9h24M50 3l6 6-6 6" fill="none" stroke="var(--red)" stroke-width="2"/></svg>
  <div class="abs laptop-screen"><div role="img" aria-label="Video still of a salvage yard"></div></div>
  <svg class="abs" style="left:805px;top:2302px" width="100" height="100"><circle cx="50" cy="50" r="44" fill="none" stroke="rgba(255,255,255,.6)" stroke-width="6"/><path d="M40 30l30 20-30 20z" fill="rgba(255,255,255,.6)"/></svg>
  <div class="abs laptop-base"></div>
</section>

<section>
  <div class="abs signup" role="img" aria-label="Dark photo of an auto parts warehouse"></div>
  <h2 class="abs display signup-title">SIGN-UP NOW!</h2>
  <div class="abs signup-sub">Sign up for our monthly newsletter and receive exclusive deals and new product alerts:</div>
  <div class="abs email">Enter You E-mail Address Here</div>
  <div class="abs subscribe">SUBSCRIBE NOW ➔</div>
</section>

<footer>
  <div class="abs site-footer"></div>
  <div class="abs fcol" style="left:98px"><h5>QUICK LINKS</h5><ul><li>Auto Parts</li><li>Submit a Part Request</li><li>Find Used Auto Parts Your Vehicle</li><li>Salvage Yard Signup</li><li>Find Salvage Yards</li><li>Parts Buying Guide</li><li>Contact Us</li><li>Privacy Policy</li><li>Satisfaction Guarantee</li><li>Terms Of Sale</li><li>Return Policy</li></ul></div>
  <div class="abs fcol" style="left:352px"><h5>SHOP BY CATEGORIES</h5><ul><li>Lorem Ipsum</li><li style="color:#fff">Simply Dummy Text</li><li>Printing and Typesetting</li><li>Industry's Standard</li><li>Dummy Text</li><li>Lorem Ipsum</li><li>Simply Dummy Text</li><li>Printing and Typesetting</li><li>Industry's Standard</li><li>Dummy Text</li><li>Industry's Standard</li></ul></div>
  <div class="abs fcol" style="left:612px"><h5>POPULAR PAGES</h5><ul><li>Lorem Ipsum</li><li>Simply Dummy Text</li><li>Printing and Typesetting</li><li>Industry's Standard</li><li>Dummy Text</li><li>Lorem Ipsum</li><li>Simply Dummy Text</li><li>Printing and Typesetting</li><li>Industry's Standard</li><li>Dummy Text</li><li>Industry's Standard</li></ul></div>
  <div class="abs fcol" style="left:869px"><h5>COMPANY INFO</h5><p>For support and business inquiries</p><p><b>Mailing Address:</b><br>Sparrowline Auto Parts<br>410 Lark Avenue Ridgeford, CA 90000</p><p><b>Phone:</b><br>1-(000) 000 0000</p><p><b>Fax:</b><br>1-(000) 000 0000</p><p><b>Email:</b><br>info@sparrowlineparts.com</p></div>
  <div class="abs pay-bar"></div>
  <div class="abs accept">WE ACCEPT: <span></span><span></span><span></span><span></span></div>
  <div class="abs social-bottom"><span></span><span></span><span></span><span></span></div>
  <div class="abs legal">Show You The Right Way To Buy Vantor Parts, Lights, Wheels, &amp; Accessories Online. Upgrade Your Vantor With Custom Carbon Fiber &amp; Angel Eyes Headlights!<br>Copyright © 2015 - <b>Pellet Yard</b>. All rights reserved.</div>
</footer>

</body>
</html>
```